QORLIN Business card. A.I. company developing trading strategies.

My name is marcello bianchi and I'm CEO and co-founder of QORLIN Research, an AI company focusing on generating Ai-driven trading strategies.
This is our website: https://qorlin-analytics.example/
Values of our company: tech & R&D driven (we're all very mathy/stats/data driven), sophisticated (we only look for sophisticated, high knowledge investors), reserved (we don't go around telling anyone what we do).
Our main product: PivotFund. A trading strategy that delivered 70% in 2022 and 20% in 2023 so far.
Our main potential clients: HNW individuals, hedge funds, asset managers, tech entrepreneur.
Target Market(s)
Hedge funds, asset managers, High Net Worth individuals, Pension funds
Contact Information for Business Card
The basic: name, job title, company name, address, mail, phone number

```html
<!DOCTYPE html>
<html lang="en">
<head>
<meta charset="utf-8">
<title>QORLIN Research — Business Card</title>
<link rel="stylesheet" href="https://fonts.googleapis.com/css2?family=Montserrat:wght@400;500;700&display=swap">
<style>
  :root {
    --stage: #3b3c3e;
    --paper: #ffffff;
    --ink: #1d1e21;
    --red: #d4142f;
    --red-light: #e3283f;
    --night-1: #15181c;
    --night-2: #2c3036;
    --mesh: #4a4f57;
  }
  * { margin: 0; padding: 0; box-sizing: border-box; }
  html, body { width: 1200px; height: 1200px; overflow: hidden; }
  body {
    background: var(--stage);
    font-family: "Montserrat", Arial, sans-serif;
    position: relative;
  }
  .card {
    position: absolute;
    left: 160px;
    width: 880px;
    height: 503px;
    border-radius: 34px;
    overflow: hidden;
  }
  /* ---------- front ---------- */
  .card-front { top: 70px; background: var(--paper); }
  .identity {
    position: absolute;
    left: 70px;
    top: 210px;
    padding-left: 22px;
    border-left: 7px solid var(--red);
  }
  .identity-name {
    color: var(--red);
    font-weight: 700;
    font-size: 36px;
    letter-spacing: 0.5px;
    line-height: 1.05;
  }
  .identity-title {
    color: var(--ink);
    font-weight: 500;
    font-size: 21px;
    margin-top: 4px;
  }
  .contact-list {
    position: absolute;
    left: 92px;
    top: 318px;
    list-style: none;
    color: var(--ink);
    font-size: 19px;
    line-height: 1.3;
  }
  .contact-item { display: flex; align-items: flex-start; gap: 12px; margin-bottom: 2px; }
  .contact-icon { width: 20px; height: 20px; flex: none; margin-top: 3px; }
  .front-brand {
    position: absolute;
    right: 110px;
    top: 120px;
    display: flex;
    align-items: center;
    gap: 14px;
  }
  .brand-name {
    font-weight: 500;
    color: var(--ink);
    font-size: 62px;
    letter-spacing: 10px;
  }
  .brand-dot { width: 14px; height: 14px; border-radius: 50%; background: var(--red); }
  .front-band-red {
    position: absolute; left: 0; bottom: 0;
    width: 60%; height: 22px; background: var(--red);
  }
  .front-band-dark {
    position: absolute; right: 0; bottom: 0;
    width: 40%; height: 22px; background: var(--ink);
  }
  /* ---------- back ---------- */
  .card-back {
    top: 627px;
    background: radial-gradient(ellipse at 60% 40%, var(--night-2), var(--night-1) 75%);
  }
  .back-texture {
    position: absolute; inset: 0;
    background: radial-gradient(ellipse at 55% 45%, rgba(90,96,106,0.35), rgba(90,96,106,0) 60%);
  }
  .back-brand {
    position: absolute;
    left: 0; right: 0; top: 190px;
    display: flex; justify-content: center; align-items: center; gap: 18px;
  }
  .back-brand .brand-name { color: var(--paper); font-size: 86px; letter-spacing: 14px; }
  .back-brand .brand-dot { width: 18px; height: 18px; }
  .back-band {
    position: absolute; left: 45%; bottom: 0;
    width: 40%; height: 24px; background: var(--red-light);
  }
</style>
</head>
<body>

<section class="card card-front" aria-label="Business card front">
  <div class="identity">
    <div class="identity-name">MARCELLO BIANCHI</div>
    <div class="identity-title">CEO &amp; CO-FOUNDER</div>
  </div>

  <ul class="contact-list">
    <li class="contact-item">
      <svg class="contact-icon" viewBox="0 0 24 24" aria-hidden="true"><path fill="#d4142f" d="M6.6 10.8a15.2 15.2 0 0 0 6.6 6.6l2.2-2.2a1 1 0 0 1 1-.25 11.4 11.4 0 0 0 3.6.57 1 1 0 0 1 1 1V20a1 1 0 0 1-1 1A17 17 0 0 1 3 4a1 1 0 0 1 1-1h3.5a1 1 0 0 1 1 1c0 1.25.2 2.45.57 3.6a1 1 0 0 1-.25 1z"/></svg>
      <span>555-014-2287</span>
    </li>
    <li class="contact-item">
      <svg class="contact-icon" viewBox="0 0 24 24" aria-hidden="true"><rect x="2" y="5" width="20" height="14" rx="1.5" fill="#d4142f"/><path d="M3 6.5l9 6.5 9-6.5" fill="none" stroke="#fff" stroke-width="1.6"/></svg>
      <span>qorlin-analytics.example</span>
    </li>
    <li class="contact-item">
      <svg class="contact-icon" viewBox="0 0 24 24" aria-hidden="true"><g fill="none" stroke="#d4142f" stroke-width="1.8"><circle cx="12" cy="12" r="9.5"/><ellipse cx="12" cy="12" rx="4.2" ry="9.5"/><path d="M2.5 12h19M4 7h16M4 17h16"/></g></svg>
      <span>careers@qorlin-analytics.example</span>
    </li>
    <li class="contact-item">
      <svg class="contact-icon" viewBox="0 0 24 24" aria-hidden="true"><path fill="#d4142f" d="M12 2a7 7 0 0 0-7 7c0 5.2 7 13 7 13s7-7.8 7-13a7 7 0 0 0-7-7zm0 9.5A2.5 2.5 0 1 1 12 6.5a2.5 2.5 0 0 1 0 5z"/></svg>
      <span>QORLIN Research<br>48 rue des Lilas 75011 Paris</span>
    </li>
  </ul>

  <div class="front-brand">
    <span class="brand-name">QORLIN</span>
    <span class="brand-dot"></span>
  </div>

  <div class="front-band-red"></div>
  <div class="front-band-dark"></div>
</section>

<section class="card card-back" aria-label="Business card back">
  <div class="back-texture" role="img" aria-label="Faint circuit-board lines and flowing wire-mesh waves across the dark background"></div>
  <div class="back-brand">
    <span class="brand-name">QORLIN</span>
    <span class="brand-dot"></span>
  </div>
  <div class="back-band"></div>
</section>

</body>
</html>
```